Peer-to-peer Car Rental Business needs a business card design

We need a business card design for a new company based in Melbourne, Australia called "Wheelnest". We enable car owners to earny money by renting out their car to others in the community/neighbourhood when their not using it.
We would like to see designs that use the colour/s blue and/or orange.
The design should communicate young, modern, fun etc.
The themes to use should be community/neighbourhood, cars, parking, airports, car rental, sharing.

Our current logo is attached.

Target Market(s)

Young adults aged 20-35, travellers, environmentally conscious, cost conscious.

Industry/Entity Type

Business

Requirements
Must have
• Must have fields for persons name, title, mobile number, email company website.

```html
<!DOCTYPE html>
<html lang="en">
<head>
<meta charset="utf-8">
<title>Wheelnest Business Card</title>
<link href="https://fonts.googleapis.com/css2?family=Open+Sans:ital,wght@0,400;0,600;1,400;1,700&display=swap" rel="stylesheet">
<style>
  :root {
    --bg: #e9e9ec;
    --card: #ffffff;
    --brand-blue: #2f4f8f;
    --band-blue: #3b3f9a;
    --band-light: #4a72bf;
    --swoosh-grey: #8d8e93;
    --text-light: #ffffff;
  }
  * { margin: 0; padding: 0; box-sizing: border-box; }
  html, body {
    width: 1200px; height: 900px; overflow: hidden;
    background: var(--bg);
    font-family: "Open Sans", Arial, sans-serif;
  }
  .stage { position: relative; width: 1200px; height: 900px; }
  .card {
    position: absolute; width: 640px; height: 365px;
    background: var(--card); border-radius: 22px; overflow: hidden;
    box-shadow: 0 6px 18px rgba(0,0,0,0.12);
  }
  .card--front { left: 80px; top: 70px; }
  .card--back { left: 480px; top: 465px; }
  .card__art { position: absolute; inset: 0; width: 100%; height: 100%; }
  .wordmark {
    position: absolute; font-weight: 400; color: var(--brand-blue);
    letter-spacing: 0.5px; line-height: 1;
  }
  .card--front .wordmark { left: 0; right: 0; top: 145px; text-align: center; font-size: 74px; }
  .card--back .wordmark { left: 90px; top: 70px; font-size: 66px; }
  .holder { position: absolute; left: 48px; top: 280px; color: var(--text-light); }
  .holder__name { font-weight: 700; font-style: italic; font-size: 22px; }
  .holder__title { font-style: italic; font-size: 18px; }
  .contacts {
    position: absolute; left: 440px; top: 208px; list-style: none;
    color: var(--text-light); font-size: 13px; line-height: 20px;
  }
  .contacts li { display: flex; align-items: flex-start; gap: 6px; }
  .contacts .icon { width: 13px; height: 13px; margin-top: 3px; flex: none; }
  .contacts .address { line-height: 17px; margin-bottom: 4px; }
</style>
</head>
<body>
<div class="stage">

  <section class="card card--front">
    <div class="wordmark">wheelnest</div>
  </section>

  <section class="card card--back">
    <svg class="card__art" viewBox="0 0 640 365" aria-hidden="true">
      <defs>
        <radialGradient id="bandGlow" cx="0.72" cy="0.55" r="0.7">
          <stop offset="0" stop-color="var(--band-light)"/>
          <stop offset="1" stop-color="var(--band-blue)"/>
        </radialGradient>
      </defs>
      <path d="M0,198 C190,268 420,240 612,102 C420,252 190,284 0,216 Z" fill="var(--swoosh-grey)"/>
      <path d="M0,228 C200,300 430,262 640,92 L640,365 L0,365 Z" fill="url(#bandGlow)"/>
    </svg>

    <div class="wordmark">wheelnest</div>

    <div class="holder">
      <div class="holder__name">Sam Porter</div>
      <div class="holder__title">Owner / C.E.O</div>
    </div>

    <ul class="contacts">
      <li class="address">
        <svg class="icon" viewBox="0 0 14 14"><circle cx="7" cy="7" r="7" fill="#fff"/><path d="M3.5,7.5 L7,4 L10.5,7.5 V10.5 H3.5 Z" fill="var(--band-blue)"/></svg>
        <span>Unit 14, Elm Court,<br>VIC 3051</span>
      </li>
      <li>
        <svg class="icon" viewBox="0 0 14 14"><circle cx="7" cy="7" r="7" fill="#fff"/><path d="M4.5,3.5 L6,3.5 L6.5,5.5 L5.6,6.2 C6.1,7.3 6.8,8 7.8,8.4 L8.5,7.5 L10.5,8 V9.5 C7,10 4,7 4.5,3.5 Z" fill="var(--band-blue)"/></svg>
        <span>0412-555-018</span>
      </li>
      <li>
        <svg class="icon" viewBox="0 0 14 14"><circle cx="7" cy="7" r="7" fill="#fff"/><rect x="4.5" y="3" width="5" height="8" rx="1" fill="var(--band-blue)"/></svg>
        <span>0398-555-274</span>
      </li>
      <li>
        <svg class="icon" viewBox="0 0 14 14"><circle cx="7" cy="7" r="7" fill="#fff"/><rect x="3.5" y="5" width="7" height="5" rx="1" fill="var(--band-blue)"/><rect x="5" y="3" width="4" height="2" fill="var(--band-blue)"/></svg>
        <span>0398-555-275</span>
      </li>
      <li>
        <svg class="icon" viewBox="0 0 14 14"><circle cx="7" cy="7" r="7" fill="#fff"/><rect x="3.5" y="4.5" width="7" height="5" fill="var(--band-blue)"/><path d="M3.5,4.5 L7,7.5 L10.5,4.5" stroke="#fff" stroke-width="0.8" fill="none"/></svg>
        <span>hello@wheelnest.com</span>
      </li>
      <li>
        <svg class="icon" viewBox="0 0 14 14"><circle cx="7" cy="7" r="7" fill="#fff"/><circle cx="7" cy="7" r="3.8" fill="none" stroke="var(--band-blue)" stroke-width="1"/><path d="M3.2,7 H10.8 M7,3.2 V10.8" stroke="var(--band-blue)" stroke-width="0.8"/></svg>
        <span>www.wheelnest.com</span>
      </li>
    </ul>
  </section>

</div>
</body>
</html>
```